Real Estate Webpage Design

We have an existing website: verindaleestates.com.au
We focus customised service mainly on Property Management and second-hand property sales.
We are not entirely happy about the current design and layout can stay roughly the same as the back end coding is linked to a CRM system.
We would like to see the design are more reachable to our clients and appearing.
Please check our Website Design Draft for more details.

Industry/Entity Type

Real estate Agency

Number of Pages Required

5+ page

Font styles to use
Sans Serif

Colors

Designer to choose colors to be used in the design.

```html
<!DOCTYPE html>
<html lang="en">
<head>
<meta charset="utf-8">
<title>Verindale Estates</title>
<link rel="stylesheet" href="https://fonts.googleapis.com/css2?family=Rubik:wght@500;600;700;800&family=Roboto:wght@400;500;700&display=swap">
<style>
:root{
  --gold:#efbd4d;
  --gold-dark:#e2ab33;
  --navy:#1f2b40;
  --navy-deep:#17223a;
  --ink:#1d1d24;
  --text:#3b3b44;
  --muted:#8a8d96;
  --white:#ffffff;
  --footer:#0f1014;
  --line:#e6e6ea;
}
*{box-sizing:border-box;margin:0;padding:0}
html,body{width:1200px;height:4135px;overflow:hidden}
body{font-family:"Roboto",Arial,sans-serif;color:var(--text);background:var(--white);position:relative}
.abs{position:absolute}
h1,h2,h3,.heading{font-family:"Rubik",Arial,sans-serif}

/* top bar & header */
.topbar{left:305px;top:0;width:895px;height:40px;background:var(--gold);clip-path:polygon(0 0,100% 0,100% 100%,34px 100%);display:flex;align-items:center;gap:36px;padding-left:100px;color:var(--white);font-size:14px;font-weight:700}
.topbar span{display:flex;align-items:center;gap:8px}
.topbar .sep{opacity:.8}
.header{left:0;top:0;width:1200px;height:114px}
.brand{left:109px;top:36px;display:flex;align-items:center;gap:12px}
.brand-mark{width:40px;height:40px;background:var(--gold)}
.brand-name{font-family:"Rubik",sans-serif;font-weight:600;font-size:28px;color:var(--gold);line-height:1}
.nav{left:376px;top:68px;display:flex;gap:27px;font-size:14px;font-weight:500;color:var(--ink)}
.lang{left:1038px;top:65px;display:flex;align-items:center;gap:10px}
.lang .flag{width:26px;height:26px;border-radius:50%;background:#2a3f86}

/* hero */
.hero{left:0;top:114px;width:1200px;height:637px;background:linear-gradient(180deg,#7fa8cf 0%,#b9cde0 38%,#8d8f8b 60%,#5f6b4d 80%,#9a9a98 100%)}
.hero-panel{left:168px;top:274px;width:422px;height:207px;background:rgba(40,44,52,.55)}
.hero-kicker{left:170px;top:306px;font-family:"Rubik",sans-serif;font-weight:700;font-size:31px;color:var(--white);letter-spacing:.5px}
.hero-title{left:168px;top:346px;font-family:"Rubik",sans-serif;font-weight:800;font-size:66px;color:var(--white);line-height:1}
.hero-copy{left:171px;top:434px;width:380px;font-size:14px;line-height:22px;color:var(--white)}
.btn{display:inline-flex;align-items:center;justify-content:center;gap:10px;font-family:"Roboto",sans-serif;font-weight:700;font-size:14px;color:var(--white);background:var(--gold)}
.hero .btn,.hero-btn{left:170px;top:504px;width:160px;height:49px}
.arrow-round{width:40px;height:40px;border-radius:50%;background:var(--white);display:flex;align-items:center;justify-content:center;border:2px solid #d9d9d9}

/* about */
.about-frame{left:137px;top:836px;width:378px;height:380px;border-top:4px solid var(--gold);border-left:4px solid var(--gold);border-top-left-radius:6px}
.about-photo{left:149px;top:847px;width:367px;height:367px;background:linear-gradient(160deg,#9cc4e2 0%,#dfe6ea 45%,#6e7a70 75%,#3f6a3a 100%);border-radius:4px}
.about-dots{left:432px;top:1066px;width:102px;height:164px;background-image:radial-gradient(var(--navy) 1.2px,transparent 1.4px);background-size:8px 8px}
.about-title{left:590px;top:838px;font-weight:700;font-size:34px;color:var(--ink)}
.about-text{left:590px;top:884px;width:472px;font-size:14.5px;line-height:25.7px;color:var(--text);text-align:justify}
.about-btn{left:590px;top:1157px;width:160px;height:50px}

/* listings */
.listings{left:0;top:1287px;width:1200px;height:691px;background:linear-gradient(180deg,#2a3650 0%,#1f2b40 60%,#26324a 100%)}
.listings-title{left:0;top:1362px;width:1200px;text-align:center;font-weight:700;font-size:33px;color:var(--white)}
.tabs{left:220px;top:1432px;display:flex;gap:10px}
.tab{width:144px;height:55px;background:var(--white);color:var(--ink);font-weight:700;font-size:14px;display:flex;align-items:center;justify-content:center}
.tab.active{background:var(--gold);color:var(--white)}
.card{width:298px;height:343px;top:1550px;background:var(--white);padding:8px}
.card-photo{height:164px;width:100%}
.card-body{padding:20px 8px 0 8px}
.suburb{font-weight:700;font-size:14px;color:var(--ink);letter-spacing:.2px}
.specs{display:flex;align-items:center;gap:10px;margin-top:14px;font-size:14px;color:var(--ink)}
.specs svg{display:block}
.addr{margin-top:12px;font-size:14px;color:var(--ink)}
.card-foot{margin-top:15px;border-top:1px solid var(--line);padding-top:16px;display:flex;justify-content:space-between;align-items:center}
.stars{display:flex;gap:3px}

/* team */
.team{left:0;top:1978px;width:1200px;height:661px;background:linear-gradient(180deg,#f4f4f6 0%,#fafafa 50%,#f0f1f3 100%)}
.team-title{left:0;top:2052px;width:1200px;text-align:center;font-weight:700;font-size:33px;color:var(--navy)}
.member{top:2148px;width:260px;text-align:center}
.portrait{width:225px;height:225px;margin:0 auto;border-radius:50%;border:5px solid var(--white);box-shadow:0 2px 8px rgba(0,0,0,.12)}
.plus{width:40px;height:40px;border-radius:50%;background:var(--white);margin:-40px auto 0;position:relative;display:flex;align-items:center;justify-content:center;box-shadow:0 1px 4px rgba(0,0,0,.2)}
.member-name{margin-top:16px;font-weight:700;font-size:14px;color:var(--ink)}
.member-role{margin-top:12px;font-size:14px;color:var(--gold)}
.team-btn{left:520px;top:2502px;width:160px;height:51px;background:var(--navy)}

/* testimonials */
.testimonials{left:0;top:2639px;width:1200px;height:571px;background:var(--gold)}
.testi-title{left:0;top:2718px;width:1200px;text-align:center;font-weight:700;font-size:33px;color:var(--white)}
.quote-card{top:2797px;width:296px;height:326px;background:var(--white);text-align:center;padding:44px 24px 0}
.avatar{width:93px;height:93px;border-radius:50%;margin:0 auto;position:relative}
.quote-badge{position:absolute;right:-14px;bottom:-8px;width:36px;height:36px;border-radius:50%;background:var(--gold);border:3px solid var(--white);display:flex;align-items:center;justify-content:center}
.quote-text{margin-top:24px;font-size:14.5px;line-height:25.6px;color:var(--text)}
.quote-name{margin-top:12px;font-weight:700;font-size:14px;color:var(--ink)}
.side-arrow{top:2948px}

/* map & contact */
.map{left:0;top:3210px;width:1200px;height:487px;background:linear-gradient(120deg,#cfe3c7 0%,#e9ecea 35%,#b9d3ec 50%,#e6e7e3 65%,#eadcc2 100%)}
.footer{left:0;top:3697px;width:1200px;height:438px;background:var(--footer)}
.contact-card{left:242px;top:3582px;width:714px;height:369px;background:var(--white)}
.contact-title{position:absolute;left:0;top:34px;width:100%;text-align:center;font-weight:700;font-size:32px;color:var(--ink)}
.contact-item{position:absolute;left:34px;display:flex;align-items:center;gap:17px;font-size:14.5px;line-height:23px;color:var(--ink)}
.ci-icon{width:32px;height:32px;border-radius:50%;background:var(--gold);display:flex;align-items:center;justify-content:center;flex:none}
.field{position:absolute;left:377px;width:303px;height:40px;border:1px solid var(--line);background:#fbfbfc;font-size:14.5px;color:var(--ink);display:flex;align-items:center;padding-left:20px}
.submit{position:absolute;left:547px;top:284px;width:132px;height:42px}
.footer-nav{left:0;top:4015px;width:1250px;display:flex;justify-content:center;gap:27px;font-size:14.5px;font-weight:500;color:var(--white)}
.footer-rule{left:112px;top:4070px;width:976px;height:1px;background:#34353c}
.copyright{left:0;top:4090px;width:1200px;text-align:center;font-size:14px;color:var(--white)}
</style>
</head>
<body>

<!-- Header -->
<div class="abs topbar">
  <span><svg width="14" height="14" viewBox="0 0 24 24"><path fill="#fff" d="M6.6 10.8a15.1 15.1 0 0 0 6.6 6.6l2.2-2.2c.3-.3.7-.4 1-.2 1.1.4 2.3.6 3.6.6.6 0 1 .4 1 1V20c0 .6-.4 1-1 1A17 17 0 0 1 3 4c0-.6.4-1 1-1h3.5c.6 0 1 .4 1 1 0 1.3.2 2.5.6 3.6.1.3 0 .7-.2 1z"/></svg>02 6204 3170</span>
  <span class="sep">|</span>
  <span><svg width="15" height="12" viewBox="0 0 24 18"><rect x="1" y="1" width="22" height="16" rx="2" fill="none" stroke="#fff" stroke-width="2"/><path d="M1 2l11 8 11-8" fill="none" stroke="#fff" stroke-width="2"/></svg>hello@verindaleestates.com.au</span>
  <span class="sep">|</span>
  <span><svg width="14" height="14" viewBox="0 0 24 24"><circle cx="12" cy="12" r="10" fill="none" stroke="#fff" stroke-width="2.4"/><path d="M12 6v6l4 2" stroke="#fff" stroke-width="2.4" fill="none"/></svg>Monday – Friday &nbsp;8:30 am – 5:00pm</span>
</div>
<div class="abs brand"><div class="brand-mark"></div><div class="brand-name">Verindale</div></div>
<nav class="abs nav"><span>HOME</span><span>ABOUT US</span><span>LEASING</span><span>BUY</span><span>SELL</span><span>OUR TEAM</span><span>BLOG</span><span>CONTACT US</span></nav>
<div class="abs lang"><div class="flag"></div><svg width="10" height="6" viewBox="0 0 10 6"><path d="M0 0h10L5 6z" fill="#1d1d24"/></svg></div>

<!-- Hero -->
<section class="abs hero" role="img" aria-label="Photo of a modern two-storey home with a garden and driveway"></section>
<div class="abs hero-panel"></div>
<div class="abs hero-kicker">WELCOME TO</div>
<h1 class="abs hero-title">VERINDALE</h1>
<p class="abs hero-copy">Helping landlords and vendor alike to complete efficient property transactions is our signature talent.</p>
<div class="abs btn" style="left:170px;top:504px;width:160px;height:49px">GET STARTED <svg width="14" height="14" viewBox="0 0 16 16"><circle cx="8" cy="8" r="8" fill="#fff"/><path d="M6.5 4.5L10 8l-3.5 3.5" stroke="#efbd4d" stroke-width="2" fill="none"/></svg></div>
<div class="abs arrow-round" style="left:41px;top:415px"><svg width="10" height="16" viewBox="0 0 10 16"><path d="M8 2L2 8l6 6" stroke="#1d1d24" stroke-width="2.4" fill="none"/></svg></div>
<div class="abs arrow-round" style="left:1117px;top:415px"><svg width="10" height="16" viewBox="0 0 10 16"><path d="M2 2l6 6-6 6" stroke="#1d1d24" stroke-width="2.4" fill="none"/></svg></div>

<!-- About -->
<div class="abs about-frame"></div>
<div class="abs about-dots"></div>
<div class="abs about-photo" role="img" aria-label="Photo of a white single-storey home with glass doors and a pool"></div>
<h2 class="abs about-title">ABOUT US</h2>
<p class="abs about-text">Verindale Estates was founded on a simple idea that a home is more than an address. Buying a property is one of the most important investments people make. Verindale is a real estate company located in Ashbury Park, Canberra. Being a portfolio sales agent and property manager, coupled with our high profile international real estate experience, Verindale is considered a market leader on the cutting edge with industry knowledge, ranging from landlord tenant relationships, residential purchases. Helping landlords and vendor alike to complete efficient property transactions is our signature talent. Our poise, precision, and insight give us an unparalleled advantage.</p>
<div class="abs btn about-btn">GET STARTED <svg width="14" height="14" viewBox="0 0 16 16"><circle cx="8" cy="8" r="8" fill="#fff"/><path d="M6.5 4.5L10 8l-3.5 3.5" stroke="#efbd4d" stroke-width="2" fill="none"/></svg></div>

<!-- Listings -->
<section class="abs listings" role="img" aria-label="Darkened photo of a living room interior behind the listings"></section>
<h2 class="abs listings-title">THIS MONTH AT VERINDALE ESTATES</h2>
<div class="abs tabs"><div class="tab">FOR SALE</div><div class="tab">FOR LEASE</div><div class="tab">OPEN TIMES</div><div class="tab active">SOLD</div><div class="tab">LEASED</div></div>

<article class="abs card" style="left:130px">
  <div class="card-photo" role="img" aria-label="Photo of a bright living room with a sofa and balcony" style="background:linear-gradient(135deg,#e9e4dc,#b9b0a3 60%,#8d7d6b)"></div>
  <div class="card-body">
    <div class="suburb">WATTLEBROOK</div>
    <div class="specs">
      <svg width="18" height="12" viewBox="0 0 18 12"><path d="M1 1v10M1 8h16v3M3 5h5v3H3zM9 5h8v3" fill="#efbd4d" stroke="#efbd4d"/></svg>3
      <svg style="margin-left:14px" width="18" height="14" viewBox="0 0 18 14"><path d="M2 7h14v3a3 3 0 0 1-3 3H5a3 3 0 0 1-3-3zM3 7V2a1 1 0 0 1 2 0" fill="#efbd4d" stroke="#efbd4d"/></svg>2
      <svg style="margin-left:14px" width="20" height="14" viewBox="0 0 20 14"><path d="M3 6l2-5h10l2 5h1v6h-3v-2H5v2H2V6z" fill="#efbd4d"/></svg>2
    </div>
    <div class="addr">12/208 Larkin Drive Wattlebrook</div>
    <div class="card-foot">
      <div class="stars"><svg width="80" height="14" viewBox="0 0 80 14"><g fill="#efbd4d"><path id="s" d="M7 0l2 4.6 5 .4-3.8 3.2 1.2 4.8L7 10.4 2.6 13l1.2-4.8L0 5l5-.4z"/><use href="#s" x="16"/><use href="#s" x="32"/><use href="#s" x="48"/><use href="#s" x="64"/></g></svg></div>
      <svg width="16" height="12" viewBox="0 0 16 12"><rect width="16" height="12" rx="1" fill="#efbd4d"/><path d="M1 1l7 5 7-5" stroke="#fff" stroke-width="1.5" fill="none"/></svg>
    </div>
  </div>
</article>

<article class="abs card" style="left:451px">
  <div class="card-photo" role="img" aria-label="Photo of a waterfront apartment building" style="background:linear-gradient(180deg,#b8d2e6,#6f8a78 55%,#3f6f78)"></div>
  <div class="card-body">
    <div class="suburb">HARBOURSIDE</div>
    <div class="specs">
      <svg width="18" height="12" viewBox="0 0 18 12"><path d="M1 1v10M1 8h16v3M3 5h5v3H3zM9 5h8v3" fill="#efbd4d" stroke="#efbd4d"/></svg>2
      <svg style="margin-left:14px" width="18" height="14" viewBox="0 0 18 14"><path d="M2 7h14v3a3 3 0 0 1-3 3H5a3 3 0 0 1-3-3zM3 7V2a1 1 0 0 1 2 0" fill="#efbd4d" stroke="#efbd4d"/></svg>2
      <svg style="margin-left:14px" width="20" height="14" viewBox="0 0 20 14"><path d="M3 6l2-5h10l2 5h1v6h-3v-2H5v2H2V6z" fill="#efbd4d"/></svg>2
    </div>
    <div class="addr">204/17 Pellin Rise Harbourside</div>
    <div class="card-foot">
      <div class="stars"><svg width="80" height="14" viewBox="0 0 80 14"><g fill="#efbd4d"><use href="#s"/><use href="#s" x="16"/><use href="#s" x="32"/><use href="#s" x="48"/><use href="#s" x="64"/></g></svg></div>
      <svg width="16" height="12" viewBox="0 0 16 12"><rect width="16" height="12" rx="1" fill="#efbd4d"/><path d="M1 1l7 5 7-5" stroke="#fff" stroke-width="1.5" fill="none"/></svg>
    </div>
  </div>
</article>

<article class="abs card" style="left:772px">
  <div class="card-photo" role="img" aria-label="Photo of an open-plan kitchen and dining room" style="background:linear-gradient(135deg,#f1efe9,#cfc6b8 55%,#8f8778)"></div>
  <div class="card-body">
    <div class="suburb">ELMSDALE</div>
    <div class="specs">
      <svg width="18" height="12" viewBox="0 0 18 12"><path d="M1 1v10M1 8h16v3M3 5h5v3H3zM9 5h8v3" fill="#efbd4d" stroke="#efbd4d"/></svg>3
      <svg style="margin-left:14px" width="18" height="14" viewBox="0 0 18 14"><path d="M2 7h14v3a3 3 0 0 1-3 3H5a3 3 0 0 1-3-3zM3 7V2a1 1 0 0 1 2 0" fill="#efbd4d" stroke="#efbd4d"/></svg>2
      <svg style="margin-left:14px" width="20" height="14" viewBox="0 0 20 14"><path d="M3 6l2-5h10l2 5h1v6h-3v-2H5v2H2V6z" fill="#efbd4d"/></svg>2
    </div>
    <div class="addr">4/9 Corran Place Elmsdale</div>
    <div class="card-foot">
      <div class="stars"><svg width="80" height="14" viewBox="0 0 80 14"><g fill="#efbd4d"><use href="#s"/><use href="#s" x="16"/><use href="#s" x="32"/><use href="#s" x="48"/><use href="#s" x="64"/></g></svg></div>
      <svg width="16" height="12" viewBox="0 0 16 12"><rect width="16" height="12" rx="1" fill="#efbd4d"/><path d="M1 1l7 5 7-5" stroke="#fff" stroke-width="1.5" fill="none"/></svg>
    </div>
  </div>
</article>
<div class="abs arrow-round" style="left:49px;top:1701px;border:none"><svg width="10" height="16" viewBox="0 0 10 16"><path d="M8 2L2 8l6 6" stroke="#1d1d24" stroke-width="2.4" fill="none"/></svg></div>
<div class="abs arrow-round" style="left:1111px;top:1701px;border:none"><svg width="10" height="16" viewBox="0 0 10 16"><path d="M2 2l6 6-6 6" stroke="#1d1d24" stroke-width="2.4" fill="none"/></svg></div>

<!-- Team -->
<section class="abs team" role="img" aria-label="Faint photo of a modern house behind the team section"></section>
<h2 class="abs team-title">OUR TEAM</h2>
<div class="abs member" style="left:95px"><div class="portrait" role="img" aria-label="Portrait of a sales agent in a dark suit" style="background:linear-gradient(180deg,#c9d6e2,#3a4150)"></div><div class="plus"><svg width="18" height="18" viewBox="0 0 18 18"><path d="M9 1v16M1 9h16" stroke="#1d1d24" stroke-width="2"/></svg></div><div class="member-name">MARCUS TAN</div><div class="member-role">Sales</div></div>
<div class="abs member" style="left:345px"><div class="portrait" role="img" aria-label="Portrait of a property sales agent in a dark blazer" style="background:linear-gradient(180deg,#d6dde6,#3d4556)"></div><div class="plus"><svg width="18" height="18" viewBox="0 0 18 18"><path d="M9 1v16M1 9h16" stroke="#1d1d24" stroke-width="2"/></svg></div><div class="member-name">LENA VO</div><div class="member-role">Property Sales</div></div>
<div class="abs member" style="left:595px"><div class="portrait" role="img" aria-label="Portrait of the marketing coordinator" style="background:linear-gradient(180deg,#eeeeee,#2f3440)"></div><div class="plus"><svg width="18" height="18" viewBox="0 0 18 18"><path d="M9 1v16M1 9h16" stroke="#1d1d24" stroke-width="2"/></svg></div><div class="member-name">GRACE LIM</div><div class="member-role">Marketing Coordinator</div></div>
<div class="abs member" style="left:844px"><div class="portrait" role="img" aria-label="Portrait of the property manager" style="background:linear-gradient(180deg,#9a9a9c,#25272d)"></div><div class="plus"><svg width="18" height="18" viewBox="0 0 18 18"><path d="M9 1v16M1 9h16" stroke="#1d1d24" stroke-width="2"/></svg></div><div class="member-name">HELEN ZHOU</div><div class="member-role">Property Manager</div></div>
<div class="abs btn team-btn">VIEW MORE <svg width="14" height="14" viewBox="0 0 16 16"><circle cx="8" cy="8" r="8" fill="#fff"/><path d="M6.5 4.5L10 8l-3.5 3.5" stroke="#1f2b40" stroke-width="2" fill="none"/></svg></div>

<!-- Testimonials -->
<section class="abs testimonials"></section>
<h2 class="abs testi-title">OUR TESTIMONIALS</h2>
<article class="abs quote-card" style="left:133px"><div class="avatar" role="img" aria-label="Portrait of a client" style="background:linear-gradient(180deg,#dcdcdc,#5a6470)"><div class="quote-badge"><svg width="14" height="12" viewBox="0 0 14 12"><path d="M0 12V7C0 3 2 1 5 0l1 2C4 3 3 4 3 6h3v6zm8 0V7c0-4 2-6 5-7l1 2c-2 1-3 2-3 4h3v6z" fill="#fff"/></svg></div></div><p class="quote-text">I would highly recommend Verindale property to you, they were helping me manage my investment property found a quality tenant in 2 days.</p><div class="quote-name">JAE PARK</div></article>
<article class="abs quote-card" style="left:452px"><div class="avatar" role="img" aria-label="Portrait of a client" style="background:linear-gradient(180deg,#5d88b3,#3a4352)"><div class="quote-badge"><svg width="14" height="12" viewBox="0 0 14 12"><path d="M0 12V7C0 3 2 1 5 0l1 2C4 3 3 4 3 6h3v6zm8 0V7c0-4 2-6 5-7l1 2c-2 1-3 2-3 4h3v6z" fill="#fff"/></svg></div></div><p class="quote-text">Very good service. Our property manager is very responsible, prompting and cares about detail. They use the system to track</p><div class="quote-name">Mei Chen</div></article>
<article class="abs quote-card" style="left:770px"><div class="avatar" role="img" aria-label="Portrait of a client" style="background:linear-gradient(180deg,#c8d8e6,#4d6074)"><div class="quote-badge"><svg width="14" height="12" viewBox="0 0 14 12"><path d="M0 12V7C0 3 2 1 5 0l1 2C4 3 3 4 3 6h3v6zm8 0V7c0-4 2-6 5-7l1 2c-2 1-3 2-3 4h3v6z" fill="#fff"/></svg></div></div><p class="quote-text">They are a greatly professional, organized and experienced team extensive knowledge understanding of the local market.My husband</p><div class="quote-name">Ruth Anne Morrow</div></article>
<svg class="abs side-arrow" style="left:62px" width="12" height="18" viewBox="0 0 12 18"><path d="M10 2L3 9l7 7" stroke="#fff" stroke-width="2.4" fill="none"/></svg>
<svg class="abs side-arrow" style="left:1124px" width="12" height="18" viewBox="0 0 12 18"><path d="M2 2l7 7-7 7" stroke="#fff" stroke-width="2.4" fill="none"/></svg>

<!-- Map & footer -->
<section class="abs map" role="img" aria-label="Street map showing the office location"></section>
<footer class="abs footer"></footer>
<div class="abs contact-card">
  <h2 class="contact-title">GET IN TOUCH</h2>
  <div class="contact-item" style="top:118px"><div class="ci-icon"><svg width="12" height="16" viewBox="0 0 12 16"><path d="M6 0a6 6 0 0 1 6 6c0 4-6 10-6 10S0 10 0 6a6 6 0 0 1 6-6z" fill="#fff"/><circle cx="6" cy="6" r="2.2" fill="#efbd4d"/></svg></div><span>18/6 Marlowe Crescent,<br>Ashbury Park, ACT, 2915</span></div>
  <div class="contact-item" style="top:197px"><div class="ci-icon"><svg width="14" height="14" viewBox="0 0 24 24"><path fill="#fff" d="M6.6 10.8a15.1 15.1 0 0 0 6.6 6.6l2.2-2.2c.3-.3.7-.4 1-.2 1.1.4 2.3.6 3.6.6.6 0 1 .4 1 1V20c0 .6-.4 1-1 1A17 17 0 0 1 3 4c0-.6.4-1 1-1h3.5c.6 0 1 .4 1 1 0 1.3.2 2.5.6 3.6.1.3 0 .7-.2 1z"/></svg></div><span>02 6204 3170</span></div>
  <div class="contact-item" style="top:266px"><div class="ci-icon"><svg width="14" height="11" viewBox="0 0 16 12"><rect x="1" y="1" width="14" height="10" rx="1" fill="none" stroke="#fff" stroke-width="1.6"/><path d="M1 2l7 5 7-5" stroke="#fff" stroke-width="1.6" fill="none"/></svg></div><span>hello@verindaleestates.com.au</span></div>
  <div class="field" style="top:117px">Name:</div>
  <div class="field" style="top:172px">Email:</div>
  <div class="field" style="top:228px">Address:</div>
  <div class="btn submit">SUBMIT <svg width="14" height="14" viewBox="0 0 16 16"><circle cx="8" cy="8" r="8" fill="#fff"/><path d="M6.5 4.5L10 8l-3.5 3.5" stroke="#efbd4d" stroke-width="2" fill="none"/></svg></div>
</div>
<nav class="abs footer-nav"><span>HOME</span><span>ABOUT US</span><span>LEASING</span><span>BUY</span><span>SELL</span><span>OUR TEAM</span><span>BLOG</span><span>CONTACT US</span></nav>
<div class="abs footer-rule"></div>
<div class="abs copyright">2022 Copyrights verindaleestates.com.au all rights reserved.</div>

</body>
</html>
```